Business Card Design Project

We are a tiling/bathroom renovation business based in Brisbane Australia and are looking to get a professional looking business card designed to promote ourselves.

We provide quality workmanship to upgrade/enhance peoples' homes.
Updates

Target Market(s)

Homeowners looking to renovate their bathrooms, or get tiling done. Mostly young adults to elderly who can spare several grand to upgrade their home

Industry/Entity Type

Business

Requirements
Must have
• A bold heading is a must: "Tiling Corvel & Dray"
Must include these details: "ABN: 41 938 106 274", "BSA Licence: 8073162", "Bastien: 0491 873 210", "Rhys: 0468 215 093", "Email: tilingcorvelanddray@quillmarsh.com", "We Lay It True And Level".

An abstract geometrical logo that's based around squares and straight lines/arrows because we are a tiling business and our slogan is "We Lay It True And Level"
Nice to have
• I have attached an image of a logo design I got from markvesta.com, and the background from Cardlorne.com.au templates I really like together I just need the cut and paste look ironed out.

You are free to play around with different looks and feels but around the same theme as my sample. i.e. simple but striking, minimal but eye catching, or not maybe something unexpected could be perfect who knows?
Should not have
• Photorealism on a business card is a pet peeve. Too much detail for a teeny tiny business card. A Business card should stand out at a distance and you shouldn't have to squint to see it's detail.

```html
<!DOCTYPE html>
<html lang="en">
<head>
<meta charset="utf-8">
<title>Tiling Corvel &amp; Dray — Business Card</title>
<link rel="stylesheet" href="https://fonts.googleapis.com/css2?family=Audiowide&family=Noto+Sans:wght@300;400;700&display=swap">
<style>
  :root {
    --page: #ffffff;
    --card-edge: #111111;
    --ink: #5f5f5f;
    --ink-soft: #6e6e6e;
    --accent-orange: #f7a21b;
  }
  html, body {
    margin: 0;
    padding: 0;
    width: 1200px;
    height: 835px;
    overflow: hidden;
    background: var(--page);
  }
  .canvas {
    position: relative;
    width: 1200px;
    height: 835px;
  }
  .card {
    display: block;
    position: absolute;
    left: 2px;
    top: 62px;
  }
  .card-heading {
    font-family: "Audiowide", sans-serif;
    font-size: 84px;
    fill: var(--ink);
  }
  .card-reg {
    font-family: "Noto Sans", sans-serif;
    font-weight: 300;
    font-size: 24px;
    fill: var(--ink-soft);
  }
  .brand-name {
    font-family: "Audiowide", sans-serif;
    font-size: 46px;
    fill: var(--ink);
  }
  .card-tagline {
    font-family: "Audiowide", sans-serif;
    font-size: 44px;
    fill: var(--ink);
  }
  .contact {
    font-family: "Noto Sans", sans-serif;
    font-size: 37px;
    fill: var(--ink-soft);
  }
  .contact-value {
    font-weight: 700;
    fill: var(--ink);
  }
</style>
</head>
<body>
<main class="canvas">
  <svg class="card" width="1196" height="663" viewBox="0 0 1196 663" xmlns="http://www.w3.org/2000/svg">
    <defs>
      <linearGradient id="tile-wash" x1="0" y1="0" x2="1" y2="1">
        <stop offset="0" stop-color="#fbe6d2"/>
        <stop offset="0.5" stop-color="#fdf4ea"/>
        <stop offset="1" stop-color="#fbe4cf"/>
      </linearGradient>
    </defs>

    <rect class="tile-background" x="1.5" y="1.5" width="1193" height="660" fill="url(#tile-wash)" role="img" aria-label="Background of pale peach and white square wall tiles in a grid"/>
    <rect class="card-border" x="1.5" y="1.5" width="1193" height="660" fill="none" stroke="var(--card-edge)" stroke-width="3"/>

    <text class="card-heading" x="45" y="120" textLength="1108" lengthAdjust="spacingAndGlyphs">TILING CORVEL &amp; DRAY</text>

    <text class="card-reg" x="145" y="150">ABN: 41 938 106 274</text>
    <text class="card-reg" x="1052" y="150" text-anchor="end">BSA Licence: 8073162</text>

    <g class="brand-mark">
      <rect x="403" y="266" width="40" height="40" fill="var(--accent-orange)"/>
      <text class="brand-name" x="461" y="303">Corvel &amp; Dray</text>
    </g>

    <text class="card-tagline" x="602" y="505" text-anchor="middle" textLength="768" lengthAdjust="spacingAndGlyphs">WE LAY IT TRUE AND LEVEL</text>

    <text class="contact" x="130" y="573">Bastien: <tspan class="contact-value">0491 873 210</tspan></text>
    <text class="contact" x="690" y="573">Rhys: <tspan class="contact-value">0468 215 093</tspan></text>
    <text class="contact" x="602" y="625" text-anchor="middle">Email: <tspan class="contact-value">tilingcorvelanddray@quillmarsh.com</tspan></text>
  </svg>
</main>
</body>
</html>
```